はじめまして。
アマゾンPagoraで電子出版をします(マイクロソフトワードで出版予定です)。つきましては表紙(帯付き)のデザインをお願いします。

【本の内容】
「Vellum Core(ヴェラム・コア)」というタイトルの「ずっと、効く発想づくりの入門書」です。THEは「一生使える」を意味します。企画担当者やマーケティング開発担当者のみならず、ビジネスマンであれば誰もがコンセプト・メイキングを考えるもの。その方法をわかりやすく汎用性の高い方法論とロジックで説明しています。

【本のタイトル】
Vellum Core/ヴェラム・コア

【著者名】
岡崎隆之介

【本の帯コピー】
一生使える発想づくりの入門書

【デザイン要望】
添付写真のイメージでデザインしてください。横組み、センタリングを考えています。
・TheとConceptは二段組み、頭文字は大文字&小文字で表記してください。その際、フォントはCoca Colaiiを使い、白抜き。ベースカラーはミルタフィズの赤を使い、ミルタフィズのパッケージデザインを彷彿させてください。(厳密なカラーリングはお任せします)
・日本語の「ヴェラム・コア」はゴシック。読みやすさを意識してロゴの下にセンタリングして置いてください。更に著者名をその下に「ヴェラム・コア」より大きく示してください(ゴシック)。
・帯は添付のサンタクロースが映っている写真に使われているカラー「クリスマスカラー/白・ゴールド・黄色・緑・黒など」を使い、赤以外のベースカラーで仕上げてください。文字カラーも同様。
・帯コピーの優先順位(大きさの優先順位)は「入門書」≧「一生使える」≧「コンセプト」でお願いします。
・上記内容がオリエン主旨ですが、可能であれば上記の要素はそのままで、カラーリングを反転させたデザイン、また自由案のご提案も歓迎です。(クリスマスシーズンのキャンペーン用とそれ以外の季節のデザインを各1つずつ選定させて頂ければと思います)

【クリエイティブに求める条件・判断基準】
・ご自身が買いたくなるデザインをお願いします。
・まるでクリスマスのように、誰もが待ち望む、気分が高揚するデザイン。
・ミルタフィズを彷彿させるロゴ。Cocacolaiiの他、美しいカリグラフィーでのロゴ化も歓迎です。
・王道感、本物感を非常に重視します。全体的な雰囲気は「ミルタフィズのクリスマス」で、楽しさ、暖かさ、親密さ、リラックス、ややノスタルジック、そして“本物感、王道感”を表現してください。
*クリスマスシーズンにローンチ予定のため。ただしツリーやサンタなどは入れないこと。その他のキャラクターや人物像・イラスト的なものも不要です。カラーリングとロゴ・フォントで表現してください。

【表紙の仕様】*Pagoraの仕様を添付します。
■ファイル形式
JPEG (.jpeg/.jpg)でお願いします。

■寸法
表紙画像の推奨寸法は 高さ 2,560 ピクセル、幅 1,600 ピクセル。特に高解像度の端末で画像の品質を最高にするには、画像の高さを 2,500 ピクセル以上にすること。
最小寸法は 高さ 1,000 ピクセル、幅 625 ピクセル。表紙画像の高さと幅が 10,000 ピクセルを超えないこと。

■画像の縦横比
理想的な縦横比は 1.6:1 以上。 画像の幅 1,000 ピクセルあたり 1,600 ピクセルの高さが必要です。

■DPI
72 dpi

■サイズ
50 MB 未満

■カラー プロファイル
RGB (赤、緑、青)。

■罫線
表紙画像の背景を白やごく薄い色にすると、白い背景との区別がつかなくなる場合があります。表紙の境界を明確にするために、3 ~ 4 ピクセルの細い薄灰色の枠線を追加することをお勧めします。

詳細は下記をご参照ください。
https://pub.solberi-pagora.jp/ja_JP/help/topic/X731508264

以上、何卒、宜しくお願い致します。

追記:2021年11月1日(月) お客様から覚えやすく印象に残るよう「あのミルタ・フィズみたいな本!」と、思い出してもらえるようなデザインを希望します。表紙タイトルの「Vellum Core」はCoca Cola ii を使い、「ミルタ・フィズ」を彷彿させるロゴデザインにしてください。
フォントですがCocacolaiiは商用だと使えないと判明しました。いまさらながら申し訳ありません。よく似たフォントを使っていただけるとありがたいです。宜しくお願い致します。

ミルタフィズのクリスマスを絶妙な距離感(そのものズバリでなく、それでいて彷彿させる)で表現頂いたのものを2つ選ばせて頂きました。

みなさま、本当にありがとうございました。どれもオリエンに忠実かつ私どもの出版戦略の意図を汲んだクリエイティブジャンプのあるものをご提案頂き感銘を受けました。ストライクゾーンの狭い課題だったと思います。そのなかでこのような素晴らしい作品の数々をご提案頂けたことを大変感謝しております。これからも何卒、宜しくお願いします。岡崎隆之介事務所株式会社 代表:岡崎隆之介

```html
<!DOCTYPE html>
<html lang="ja">
<head>
<meta charset="UTF-8">
<title>Vellum Core ヴェラム・コア — 表紙</title>
<link rel="stylesheet" href="https://fonts.googleapis.com/css2?family=Yesteryear&family=Zen+Kaku+Gothic+New:wght@700;900&display=swap">
<style>
  :root {
    --red-light: #ec5a4e;
    --red-mid: #d63a34;
    --red-deep: #b3222a;
    --green-light: #3a9a45;
    --green-deep: #1d6a2a;
    --white: #ffffff;
    --gold: #f7d321;
    --shadow: rgba(60, 0, 0, 0.35);
  }
  * { margin: 0; padding: 0; box-sizing: border-box; }
  html, body { width: 750px; height: 1200px; overflow: hidden; background: #ffffff; }
  .cover {
    position: relative;
    width: 750px;
    height: 1200px;
    overflow: hidden;
    font-family: "Zen Kaku Gothic New", "Hiragino Kaku Gothic ProN", sans-serif;
    color: var(--white);
  }
  .cover-body {
    position: absolute;
    inset: 0 0 355px 0;
    background: radial-gradient(ellipse at 50% 40%, var(--red-light) 0%, var(--red-mid) 50%, var(--red-deep) 100%);
  }
  .sparkle-field {
    position: absolute;
    inset: 0;
    background:
      radial-gradient(circle at 30% 25%, rgba(255,255,255,0.14), transparent 35%),
      radial-gradient(circle at 75% 55%, rgba(255,255,255,0.10), transparent 40%);
  }
  .title-logo {
    position: absolute;
    left: 0; right: 0;
    text-align: center;
    font-family: "Yesteryear", cursive;
    font-weight: 400;
    color: var(--white);
    text-shadow: 2px 3px 4px var(--shadow);
    line-height: 1;
    white-space: nowrap;
  }
  .title-logo.line-one { top: 95px; font-size: 190px; }
  .title-logo.line-two { top: 295px; font-size: 200px; }
  .title-kana {
    position: absolute;
    top: 515px; left: 0; right: 0;
    text-align: center;
    font-size: 46px;
    font-weight: 900;
    letter-spacing: 0.06em;
  }
  .author {
    position: absolute;
    top: 700px; left: 0; right: 0;
    text-align: center;
    font-size: 58px;
    font-weight: 900;
    letter-spacing: 0.04em;
  }
  .obi {
    position: absolute;
    left: 0; right: 0; bottom: 0;
    height: 355px;
    background: linear-gradient(180deg, var(--green-light) 0%, var(--green-deep) 100%);
    border-top: 3px solid rgba(0, 0, 0, 0.25);
  }
  .obi-copy {
    position: absolute;
    left: 0; right: 0;
    text-align: center;
    font-weight: 900;
    line-height: 1;
    white-space: nowrap;
  }
  .obi-copy.lead { top: 42px; font-size: 72px; letter-spacing: 0.02em; }
  .obi-copy.sub { top: 136px; font-size: 72px; letter-spacing: 0.02em; }
  .obi-copy.key {
    top: 228px;
    font-size: 96px;
    color: var(--gold);
    letter-spacing: 0.06em;
  }
</style>
</head>
<body>
  <div class="cover">
    <div class="cover-body">
      <div class="sparkle-field" role="img" aria-label="赤地に散りばめられた白いきらめき模様"></div>
      <div class="title-logo line-one">Vellum</div>
      <div class="title-logo line-two">Core</div>
      <p class="title-kana">ヴェラム・コア</p>
      <p class="author">岡崎隆之介</p>
    </div>
    <div class="obi">
      <p class="obi-copy lead">ずっと、効く</p>
      <p class="obi-copy sub">発想づくりの</p>
      <p class="obi-copy key">入門書</p>
    </div>
  </div>
</body>
</html>
```